Redesign the Eshop of a gift shop

We want to redesign the front page, the category page and the product page of our Eshop that sells gifts.
I am thinking not to reveal the url of the eshop as i don't want you to get influenced. Lets call the Eshop "PresentNest.com"
I will list the brands that we resell so you understand what we are selling,
Morvato-https://www.morvato-example.com/
Zandorpel-https://zandorpel-example.com/
Vamtol - https://vamtol-example.com/
Quiet Orchard - https://www.quietorchard-example.com/
Ranger's Workbench - https://rangersworkbench-example.com/
Plumeline press - https://plumelinepress-example.com/
Tarpawn - https://tarpawnofficial-example.com/
We also sell toys for adults like backgamon, chess, playing cards, board games.
The problem is that many eshops sell these and thats why i would like the design to have a different approach, more fresh, not seen before.
I am also thinking of something playfull, happy, but warm at the same time.
Please note that our logo is black & white but feel free to play with any color/s you like in your website design. We might eventually even adjust the logo colors, or you can provide a pallete that suites a black and white logo
Let me know if you have any questions!
Updates
A couple of designers kindly asked to extend so they can submit.
Target Market(s)
Age: 20-50, Gender: Also men but mostly women, Income: Moderate to high, Interests and Lifestyle: Customers who value sentimentality, personal connection, and thoughtful gestures, Relationship Status: Those in relationships or with larger families
Number of Pages Required
3 page
Look and feel
Each slider illustrates characteristics of the customer's brand and the style your logo design should communicate.

```html
<!DOCTYPE html>
<html lang="en">
<head>
<meta charset="utf-8">
<title>Stationeries – PresentNest</title>
<link href="https://fonts.googleapis.com/css2?family=Outfit:wght@300;400;500;600&display=swap" rel="stylesheet">
<style>
:root{
  --ink:#111318;
  --text:#2a2c33;
  --muted:#8a8d96;
  --line:#d9dbe0;
  --soft:#f4f5f8;
  --panel:#f6f7fa;
  --star:#f59e0b;
  --accent:#2563eb;
  --badge:#fde8e8;
  --badge-text:#e35d5d;
  --navy:#111827;
}
*{box-sizing:border-box;margin:0;padding:0}
html,body{width:1200px;height:4182px;overflow:hidden;background:#fff}
body{font-family:"Outfit",sans-serif;color:var(--text);position:relative}
.abs{position:absolute}

/* header */
.logo{left:83px;top:26px;font-size:24px;font-weight:300;letter-spacing:2px;color:var(--ink);display:flex;align-items:center;gap:8px}
.logo .mark{width:12px;height:12px;background:var(--ink)}
.search{left:428px;top:20px;width:332px;height:38px;border-radius:19px;background:var(--soft);display:flex;align-items:center;gap:10px;padding-left:16px;font-size:13px;color:var(--muted)}
.actions{left:783px;top:20px;height:38px;display:flex;align-items:center;gap:30px;font-size:13px;color:var(--text)}
.actions span{display:flex;align-items:center;gap:8px}
.avatar{left:1077px;top:20px;width:38px;height:38px;border-radius:50%;background:linear-gradient(135deg,#c9c6c2,#8e8a86)}
.nav{left:174px;top:76px;display:flex;font-size:13px;color:var(--text)}
.nav a{color:inherit;text-decoration:none;display:flex;align-items:center;gap:8px;margin-right:28px}

/* banner */
.banner{left:83px;top:133px;width:1032px;height:180px;border-radius:24px;overflow:hidden;display:flex;align-items:center;justify-content:center;
  background:linear-gradient(100deg,#a88f92 0%,#b89ea1 20%,#8fb1ac 35%,#a9c9ad 55%,#9fbfa3 75%,#b49ea1 100%)}
.banner h1{font-size:50px;font-weight:500;color:#fff}

/* heading */
.page-title{left:83px;top:368px;display:flex;align-items:center;gap:16px}
.page-title h2{font-size:33px;font-weight:500;color:var(--ink)}
.count{background:var(--soft);border-radius:14px;padding:6px 12px;font-size:11px}
.sort{left:996px;top:367px;width:119px;height:43px;border:1px solid var(--line);border-radius:22px;display:flex;align-items:center;justify-content:center;gap:8px;font-size:11px}

/* sidebar */
.filters{left:83px;top:457px;width:237px;height:391px;background:var(--panel);border-radius:22px;padding:22px 20px}
.filters h3{font-size:14px;font-weight:500;color:var(--ink);margin-bottom:12px}
.check{display:flex;align-items:center;gap:10px;font-size:12px;font-weight:300;color:var(--muted);height:30px}
.box{width:16px;height:16px;border-radius:4px;border:1px solid var(--line);background:#fff;display:flex;align-items:center;justify-content:center}
.box.on{background:var(--ink);border-color:var(--ink)}
.check.on{color:var(--text)}
.gap{height:16px}
.price-title{margin-top:22px}
.price-inputs{display:flex;gap:12px}
.price-inputs span{width:92px;height:38px;border-radius:19px;background:#eceef2;display:flex;align-items:center;padding-left:16px;font-size:12px;color:var(--muted)}

/* product cards */
.grid{display:grid;column-gap:26px}
.grid.three{left:347px;top:470px;grid-template-columns:repeat(3,238px)}
.grid.three .card{height:417px}
.grid.four{left:83px;grid-template-columns:repeat(4,238px)}
.card{width:238px;position:relative}
.media{height:220px;position:relative;display:flex;align-items:center;justify-content:center}
.tag{position:absolute;left:20px;top:8px;background:var(--badge);color:var(--badge-text);font-size:9px;padding:3px 7px;border-radius:8px}
.fav{position:absolute;right:20px;top:6px;width:24px;height:24px;border-radius:50%;border:1px solid var(--line);display:flex;align-items:center;justify-content:center;background:#fff}
.ph.bag{width:104px;height:170px;border-radius:18px;background:linear-gradient(180deg,#b7a3d6 0%,#2a2730 30%,#1f1d24 100%)}
.ph.wallet{width:110px;height:185px;border-radius:10px;background:linear-gradient(160deg,#4a4b50,#26272b)}
.ph.tube{width:92px;height:170px;border-radius:12px;background:linear-gradient(180deg,#d9a640 0%,#e9a887 15%,#6aa6c4 45%,#eeb18d 80%)}
.ph.blanket{width:190px;height:170px;border-radius:10px;background:linear-gradient(160deg,#8c97a6 0%,#c7553a 35%,#d43c3c 60%,#bd6a3b 100%)}
.name{margin-top:28px;font-size:14px;font-weight:300;line-height:23px;color:var(--ink);height:46px;overflow:hidden;display:-webkit-box;-webkit-line-clamp:2;-webkit-box-orient:vertical}
.stars{margin-top:8px;display:flex;gap:2px;height:18px}
.buy{margin-top:12px;display:flex;align-items:center;justify-content:space-between}
.price{font-size:20px;font-weight:500;color:var(--ink)}
.btn{width:120px;height:42px;border:1px solid var(--line);border-radius:21px;display:flex;align-items:center;justify-content:center;font-size:10px;font-weight:500;letter-spacing:.3px;color:var(--ink);background:#fff}
.btn.dark{background:var(--navy);color:#fff;border-color:var(--navy)}

.show-more{left:0;width:1200px;top:2566px;text-align:center;font-size:11px;color:var(--accent)}
.section-title{left:83px;font-size:33px;font-weight:500;color:var(--ink)}
.see-more{right:85px;font-size:12px;color:var(--accent)}

/* footer */
.footer{left:0;top:3763px;width:1200px;height:419px;background:var(--panel)}
.footer .logo{top:105px}
.join{left:83px;top:168px;width:340px}
.join h4{font-size:13px;font-weight:500;color:var(--ink);margin-bottom:10px}
.join p{font-size:10px;font-weight:300;line-height:16px;color:var(--muted)}
.subscribe{left:83px;top:246px;display:flex;gap:8px}
.subscribe .email{width:215px;height:36px;border-radius:18px;background:#eceef2;font-size:10px;color:var(--muted);padding-left:14px;display:flex;align-items:center}
.subscribe .go{width:105px;height:36px;border-radius:18px;background:var(--navy);color:#fff;font-size:11px;display:flex;align-items:center;justify-content:center}
.socials{left:83px;top:320px;display:flex;gap:34px}
.socials span{width:16px;height:16px;border-radius:50%;border:1.6px solid var(--ink)}
.fcol{top:92px;font-size:11px;font-weight:300;color:var(--muted)}
.fcol h5{font-size:13px;font-weight:500;color:var(--ink);margin-bottom:20px}
.fcol li{list-style:none;height:37px}
</style>
</head>
<body>

<svg width="0" height="0" style="position:absolute">
  <defs>
    <symbol id="star" viewBox="0 0 20 20"><path d="M10 1.5l2.6 5.4 5.9.8-4.3 4.1 1 5.8L10 14.8l-5.2 2.8 1-5.8L1.5 7.7l5.9-.8z" fill="#f59e0b"/></symbol>
    <symbol id="heart" viewBox="0 0 20 20"><path d="M10 16.5s-6.5-4-6.5-8.5A3.5 3.5 0 0 1 10 5.8 3.5 3.5 0 0 1 16.5 8c0 4.5-6.5 8.5-6.5 8.5z" fill="none" stroke="#111318" stroke-width="1.6" stroke-linejoin="round"/></symbol>
    <symbol id="chev" viewBox="0 0 12 12"><path d="M3 4.5l3 3 3-3" fill="none" stroke="#2a2c33" stroke-width="1.4" stroke-linecap="round"/></symbol>
  </defs>
</svg>

<header>
  <div class="abs logo"><span class="mark"></span>PRESENTNEST</div>
  <div class="abs search">
    <svg width="16" height="16" viewBox="0 0 16 16"><circle cx="7" cy="7" r="5" fill="none" stroke="#8a8d96" stroke-width="1.5"/><path d="M11 11l3.5 3.5" stroke="#8a8d96" stroke-width="1.5" stroke-linecap="round"/></svg>
    Search all products
  </div>
  <div class="abs actions">
    <span><svg width="18" height="18"><use href="#heart"/></svg>Wishlist</span>
    <span><svg width="18" height="18" viewBox="0 0 18 18"><path d="M4.5 13V8a4.5 4.5 0 0 1 9 0v5l1.5 1.5h-12zM7.5 16h3" fill="none" stroke="#111318" stroke-width="1.5" stroke-linejoin="round"/></svg>Notifications</span>
    <span><svg width="18" height="18" viewBox="0 0 18 18"><path d="M3.5 6h11l-.8 10H4.3zM6.5 6V5a2.5 2.5 0 0 1 5 0v1" fill="none" stroke="#111318" stroke-width="1.5" stroke-linejoin="round"/></svg>Bag</span>
  </div>
  <div class="abs avatar" role="img" aria-label="Account profile photo"></div>
  <nav class="abs nav">
    <a>All Categories</a>
    <a>Gifts for him <svg width="12" height="12"><use href="#chev"/></svg></a>
    <a>Gifts for her <svg width="12" height="12"><use href="#chev"/></svg></a>
    <a>Home &amp; Lifestyle <svg width="12" height="12"><use href="#chev"/></svg></a>
    <a>Outdoor <svg width="12" height="12"><use href="#chev"/></svg></a>
    <a>Stationeries <svg width="12" height="12"><use href="#chev"/></svg></a>
    <a>Toys &amp; Games <svg width="12" height="12"><use href="#chev"/></svg></a>
  </nav>
</header>

<section class="abs banner" role="img" aria-label="Pastel notebooks held in a hand">
  <h1>Stationeries</h1>
</section>

<div class="abs page-title"><h2>Stationeries</h2><span class="count">345 products</span></div>
<div class="abs sort">SORT BY <svg width="12" height="12"><use href="#chev"/></svg></div>

<aside class="abs filters">
  <h3>Sub-Category</h3>
  <div class="check on"><span class="box on"><svg width="10" height="10" viewBox="0 0 10 10"><path d="M2 5.2l2 2 4-4.4" fill="none" stroke="#fff" stroke-width="1.6"/></svg></span>Journals</div>
  <div class="check"><span class="box"></span>Wellness Journals</div>
  <div class="check on"><span class="box on"><svg width="10" height="10" viewBox="0 0 10 10"><path d="M2 5.2l2 2 4-4.4" fill="none" stroke="#fff" stroke-width="1.6"/></svg></span>Notebooks</div>
  <div class="check on"><span class="box on"><svg width="10" height="10" viewBox="0 0 10 10"><path d="M2 5.2l2 2 4-4.4" fill="none" stroke="#fff" stroke-width="1.6"/></svg></span>Note Pad</div>
  <div class="check"><span class="box"></span>Folios</div>
  <div class="check"><span class="box"></span>Meal Planners</div>
  <div class="gap"></div>
  <div class="check on"><span class="box on"><svg width="10" height="10" viewBox="0 0 10 10"><path d="M2 5.2l2 2 4-4.4" fill="none" stroke="#fff" stroke-width="1.6"/></svg></span>Show in stock only</div>
  <h3 class="price-title">Price</h3>
  <div class="price-inputs"><span>$ &nbsp;From</span><span>$ &nbsp;To</span></div>
</aside>

<main class="abs grid three">
  <article class="card"><div class="media"><span class="tag">New</span><span class="fav"><svg width="14" height="14"><use href="#heart"/></svg></span><div class="ph bag" role="img" aria-label="Black backpack with purple straps"></div></div><h4 class="name">Pastello Tarpawn X Moonbun Series</h4><div class="stars"><svg width="18" height="18"><use href="#star"/></svg><svg width="18" height="18"><use href="#star"/></svg><svg width="18" height="18"><use href="#star"/></svg></div><div class="buy"><span class="price">$35.50</span><span class="btn">ADD TO BAG</span></div></article>
  <article class="card"><div class="media"><span class="fav"><svg width="14" height="14"><use href="#heart"/></svg></span><div class="ph wallet" role="img" aria-label="Grey slim leather wallet"></div></div><h4 class="name">Vamtol's Slim Leather Wallet - Original Grey</h4><div class="stars"><svg width="18" height="18"><use href="#star"/></svg><svg width="18" height="18"><use href="#star"/></svg><svg width="18" height="18"><use href="#star"/></svg><svg width="18" height="18"><use href="#star"/></svg><svg width="18" height="18"><use href="#star"/></svg></div><div class="buy"><span class="price">$20.50</span><span class="btn dark">ADD TO BAG</span></div></article>
  <article class="card"><div class="media"><span class="fav"><svg width="14" height="14"><use href="#heart"/></svg></span><div class="ph tube" role="img" aria-label="Jigsaw puzzle tube with coastal town print"></div></div><h4 class="name">Hallberg Group 500 Pieces Jigsaw Puzzle - Italy</h4><div class="stars"><svg width="18" height="18"><use href="#star"/></svg><svg width="18" height="18"><use href="#star"/></svg><svg width="18" height="18"><use href="#star"/></svg><svg width="18" height="18"><use href="#star"/></svg><svg width="18" height="18"><use href="#star"/></svg></div><div class="buy"><span class="price">$24.00</span><span class="btn">ADD TO BAG</span></div></article>

  <article class="card"><div class="media"><span class="tag">New</span><span class="fav"><svg width="14" height="14"><use href="#heart"/></svg></span><div class="ph bag" role="img" aria-label="Black backpack with purple straps"></div></div><h4 class="name">Pastello Tarpawn X Moonbun Series</h4><div class="stars"><svg width="18" height="18"><use href="#star"/></svg><svg width="18" height="18"><use href="#star"/></svg><svg width="18" height="18"><use href="#star"/></svg></div><div class="buy"><span class="price">$35.50</span><span class="btn">ADD TO BAG</span></div></article>
  <article class="card"><div class="media"><span class="fav"><svg width="14" height="14"><use href="#heart"/></svg></span><div class="ph wallet" role="img" aria-label="Grey slim leather wallet"></div></div><h4 class="name">Vamtol's Slim Leather Wallet - Original Grey</h4><div class="stars"><svg width="18" height="18"><use href="#star"/></svg><svg width="18" height="18"><use href="#star"/></svg><svg width="18" height="18"><use href="#star"/></svg><svg width="18" height="18"><use href="#star"/></svg><svg width="18" height="18"><use href="#star"/></svg></div><div class="buy"><span class="price">$20.50</span><span class="btn">ADD TO BAG</span></div></article>
  <article class="card"><div class="media"><span class="fav"><svg width="14" height="14"><use href="#heart"/></svg></span><div class="ph tube" role="img" aria-label="Jigsaw puzzle tube with coastal town print"></div></div><h4 class="name">Hallberg Group 500 Pieces Jigsaw Puzzle - Italy</h4><div class="stars"><svg width="18" height="18"><use href="#star"/></svg><svg width="18" height="18"><use href="#star"/></svg><svg width="18" height="18"><use href="#star"/></svg><svg width="18" height="18"><use href="#star"/></svg><svg width="18" height="18"><use href="#star"/></svg></div><div class="buy"><span class="price">$24.00</span><span class="btn">ADD TO BAG</span></div></article>

  <article class="card"><div class="media"><span class="tag">New</span><span class="fav"><svg width="14" height="14"><use href="#heart"/></svg></span><div class="ph bag" role="img" aria-label="Black backpack with purple straps"></div></div><h4 class="name">Pastello Tarpawn X Moonbun Series</h4><div class="stars"><svg width="18" height="18"><use href="#star"/></svg><svg width="18" height="18"><use href="#star"/></svg><svg width="18" height="18"><use href="#star"/></svg></div><div class="buy"><span class="price">$35.50</span><span class="btn">ADD TO BAG</span></div></article>
  <article class="card"><div class="media"><span class="fav"><svg width="14" height="14"><use href="#heart"/></svg></span><div class="ph wallet" role="img" aria-label="Grey slim leather wallet"></div></div><h4 class="name">Vamtol's Slim Leather Wallet - Original Grey</h4><div class="stars"><svg width="18" height="18"><use href="#star"/></svg><svg width="18" height="18"><use href="#star"/></svg><svg width="18" height="18"><use href="#star"/></svg><svg width="18" height="18"><use href="#star"/></svg><svg width="18" height="18"><use href="#star"/></svg></div><div class="buy"><span class="price">$20.50</span><span class="btn">ADD TO BAG</span></div></article>
  <article class="card"><div class="media"><span class="fav"><svg width="14" height="14"><use href="#heart"/></svg></span><div class="ph tube" role="img" aria-label="Jigsaw puzzle tube with coastal town print"></div></div><h4 class="name">Hallberg Group 500 Pieces Jigsaw Puzzle - Italy</h4><div class="stars"><svg width="18" height="18"><use href="#star"/></svg><svg width="18" height="18"><use href="#star"/></svg><svg width="18" height="18"><use href="#star"/></svg><svg width="18" height="18"><use href="#star"/></svg><svg width="18" height="18"><use href="#star"/></svg></div><div class="buy"><span class="price">$24.00</span><span class="btn">ADD TO BAG</span></div></article>

  <article class="card"><div class="media"><span class="tag">New</span><span class="fav"><svg width="14" height="14"><use href="#heart"/></svg></span><div class="ph bag" role="img" aria-label="Black backpack with purple straps"></div></div><h4 class="name">Pastello Tarpawn X Moonbun Series</h4><div class="stars"><svg width="18" height="18"><use href="#star"/></svg><svg width="18" height="18"><use href="#star"/></svg><svg width="18" height="18"><use href="#star"/></svg></div><div class="buy"><span class="price">$35.50</span><span class="btn">ADD TO BAG</span></div></article>
  <article class="card"><div class="media"><span class="fav"><svg width="14" height="14"><use href="#heart"/></svg></span><div class="ph wallet" role="img" aria-label="Grey slim leather wallet"></div></div><h4 class="name">Vamtol's Slim Leather Wallet - Original Grey</h4><div class="stars"><svg width="18" height="18"><use href="#star"/></svg><svg width="18" height="18"><use href="#star"/></svg><svg width="18" height="18"><use href="#star"/></svg><svg width="18" height="18"><use href="#star"/></svg><svg width="18" height="18"><use href="#star"/></svg></div><div class="buy"><span class="price">$20.50</span><span class="btn">ADD TO BAG</span></div></article>
  <article class="card"><div class="media"><span class="fav"><svg width="14" height="14"><use href="#heart"/></svg></span><div class="ph tube" role="img" aria-label="Jigsaw puzzle tube with coastal town print"></div></div><h4 class="name">Hallberg Group 500 Pieces Jigsaw Puzzle - Italy</h4><div class="stars"><svg width="18" height="18"><use href="#star"/></svg><svg width="18" height="18"><use href="#star"/></svg><svg width="18" height="18"><use href="#star"/></svg><svg width="18" height="18"><use href="#star"/></svg><svg width="18" height="18"><use href="#star"/></svg></div><div class="buy"><span class="price">$24.00</span><span class="btn">ADD TO BAG</span></div></article>

  <article class="card"><div class="media"><span class="tag">New</span><span class="fav"><svg width="14" height="14"><use href="#heart"/></svg></span><div class="ph bag" role="img" aria-label="Black backpack with purple straps"></div></div><h4 class="name">Pastello Tarpawn X Moonbun Series</h4><div class="stars"><svg width="18" height="18"><use href="#star"/></svg><svg width="18" height="18"><use href="#star"/></svg><svg width="18" height="18"><use href="#star"/></svg></div><div class="buy"><span class="price">$35.50</span><span class="btn">ADD TO BAG</span></div></article>
  <article class="card"><div class="media"><span class="fav"><svg width="14" height="14"><use href="#heart"/></svg></span><div class="ph wallet" role="img" aria-label="Grey slim leather wallet"></div></div><h4 class="name">Vamtol's Slim Leather Wallet - Original Grey</h4><div class="stars"><svg width="18" height="18"><use href="#star"/></svg><svg width="18" height="18"><use href="#star"/></svg><svg width="18" height="18"><use href="#star"/></svg><svg width="18" height="18"><use href="#star"/></svg><svg width="18" height="18"><use href="#star"/></svg></div><div class="buy"><span class="price">$20.50</span><span class="btn">ADD TO BAG</span></div></article>
  <article class="card"><div class="media"><span class="fav"><svg width="14" height="14"><use href="#heart"/></svg></span><div class="ph tube" role="img" aria-label="Jigsaw puzzle tube with coastal town print"></div></div><h4 class="name">Hallberg Group 500 Pieces Jigsaw Puzzle - Italy</h4><div class="stars"><svg width="18" height="18"><use href="#star"/></svg><svg width="18" height="18"><use href="#star"/></svg><svg width="18" height="18"><use href="#star"/></svg><svg width="18" height="18"><use href="#star"/></svg><svg width="18" height="18"><use href="#star"/></svg></div><div class="buy"><span class="price">$24.00</span><span class="btn">ADD TO BAG</span></div></article>
</main>

<div class="abs show-more">Show More</div>

<h2 class="abs section-title" style="top:2690px">Recommended For You</h2>
<span class="abs see-more" style="top:2712px">See More</span>
<section class="abs grid four" style="top:2790px">
  <article class="card"><div class="media"><span class="tag">New</span><span class="fav"><svg width="14" height="14"><use href="#heart"/></svg></span><div class="ph blanket" role="img" aria-label="Red gingham picnic blanket in its pack"></div></div><h4 class="name">Zandorpel Folding Portable Gingham Waterproof Picnic Blanket</h4><div class="stars"><svg width="18" height="18"><use href="#star"/></svg><svg width="18" height="18"><use href="#star"/></svg><svg width="18" height="18"><use href="#star"/></svg><svg width="18" height="18"><use href="#star"/></svg><svg width="18" height="18"><use href="#star"/></svg></div><div class="buy"><span class="price">$22.50</span><span class="btn">ADD TO BAG</span></div></article>
  <article class="card"><div class="media"><span class="tag">New</span><span class="fav"><svg width="14" height="14"><use href="#heart"/></svg></span><div class="ph bag" role="img" aria-label="Black backpack with purple straps"></div></div><h4 class="name">Pastello Tarpawn X Moonbun Series</h4><div class="stars"><svg width="18" height="18"><use href="#star"/></svg><svg width="18" height="18"><use href="#star"/></svg><svg width="18" height="18"><use href="#star"/></svg></div><div class="buy"><span class="price">$37.50</span><span class="btn">ADD TO BAG</span></div></article>
  <article class="card"><div class="media"><span class="tag">New</span><span class="fav"><svg width="14" height="14"><use href="#heart"/></svg></span><div class="ph wallet" role="img" aria-label="Grey slim leather wallet"></div></div><h4 class="name">Vamtol's Slim Leather Wallet - Original Grey</h4><div class="stars"><svg width="18" height="18"><use href="#star"/></svg><svg width="18" height="18"><use href="#star"/></svg><svg width="18" height="18"><use href="#star"/></svg><svg width="18" height="18"><use href="#star"/></svg><svg width="18" height="18"><use href="#star"/></svg></div><div class="buy"><span class="price">$20.50</span><span class="btn">ADD TO BAG</span></div></article>
  <article class="card"><div class="media"><span class="tag">New</span><span class="fav"><svg width="14" height="14"><use href="#heart"/></svg></span><div class="ph tube" role="img" aria-label="Jigsaw puzzle tube with coastal town print"></div></div><h4 class="name">Hallberg Group 500 Pieces Jigsaw Puzzle - Italy</h4><div class="stars"><svg width="18" height="18"><use href="#star"/></svg><svg width="18" height="18"><use href="#star"/></svg><svg width="18" height="18"><use href="#star"/></svg><svg width="18" height="18"><use href="#star"/></svg><svg width="18" height="18"><use href="#star"/></svg></div><div class="buy"><span class="price">$24.00</span><span class="btn">ADD TO BAG</span></div></article>
</section>

<h2 class="abs section-title" style="top:3267px">New Arrivals</h2>
<span class="abs see-more" style="top:3289px">See More</span>
<section class="abs grid four" style="top:3367px">
  <article class="card"><div class="media"><span class="tag">New</span><span class="fav"><svg width="14" height="14"><use href="#heart"/></svg></span><div class="ph blanket" role="img" aria-label="Red gingham picnic blanket in its pack"></div></div><h4 class="name">Zandorpel Folding Portable Gingham Waterproof Picnic Blanket</h4><div class="buy" style="margin-top:20px"><span class="price">$22.50</span><span class="btn">ADD TO BAG</span></div></article>
  <article class="card"><div class="media"><span class="tag">New</span><span class="fav"><svg width="14" height="14"><use href="#heart"/></svg></span><div class="ph bag" role="img" aria-label="Black backpack with purple straps"></div></div><h4 class="name">Pastello Tarpawn X Moonbun Series</h4><div class="buy" style="margin-top:20px"><span class="price">$37.50</span><span class="btn">ADD TO BAG</span></div></article>
  <article class="card"><div class="media"><span class="tag">New</span><span class="fav"><svg width="14" height="14"><use href="#heart"/></svg></span><div class="ph wallet" role="img" aria-label="Grey slim leather wallet"></div></div><h4 class="name">Vamtol's Slim Leather Wallet - Original Grey</h4><div class="buy" style="margin-top:20px"><span class="price">$20.50</span><span class="btn">ADD TO BAG</span></div></article>
  <article class="card"><div class="media"><span class="tag">New</span><span class="fav"><svg width="14" height="14"><use href="#heart"/></svg></span><div class="ph tube" role="img" aria-label="Jigsaw puzzle tube with coastal town print"></div></div><h4 class="name">Hallberg Group 500 Pieces Jigsaw Puzzle - Italy</h4><div class="buy" style="margin-top:20px"><span class="price">$24.00</span><span class="btn">ADD TO BAG</span></div></article>
</section>

<footer class="abs footer">
  <div class="abs logo"><span class="mark"></span>PRESENTNEST</div>
  <div class="abs join">
    <h4>Join Our Community Today!</h4>
    <p>Sign up for our newsletter, you'll gain access to personalized recommendations that will enhance your shopping experience.</p>
  </div>
  <div class="abs subscribe"><span class="email">Enter Email</span><span class="go">Subscribe</span></div>
  <div class="abs socials"><span aria-label="Social link"></span><span aria-label="Social link"></span><span aria-label="Social link"></span></div>
  <div class="abs fcol" style="left:624px"><h5>Services</h5><ul><li>Email Marketing</li><li>Campaigns</li><li>Branding</li><li>Offline</li></ul></div>
  <div class="abs fcol" style="left:856px"><h5>About</h5><ul><li>Our Story</li><li>Benefits</li><li>Team</li><li>Careers</li></ul></div>
  <div class="abs fcol" style="left:1050px"><h5>Help</h5><ul><li>FAQs</li><li>Contact Us</li></ul></div>
</footer>

</body>
</html>
```